WordPress website design for wealth management company

A modern clean look website for a service company. This is mostly for information only, with a form to capture prospect contact information and schedule a 15 minutes call. There will be several static pages describe what services we offer, how we are different, and a blog section for posting articles and share resources. A section for client testimonials.
I want a website that is easy to understand and maintain. No proprietary plugins that cost extra. The main thing I need help is the visual layout / color palette that present a clean and professional look, select the suitable stock photos that convey the image of trust, professional, innovative, and high service.
Some websites with style I like include the following
- https://www.morvanhollis.com/
- https://www.tindlebrookplanningworks.com/
- https://quorvalfunds.com/private-equity-partners/
Also some websites in other industries with clean modern look
- https://plotwhirl.com/
- https://dabrix.com/
- https://www.fennelroost.com/
I want the end product to be a fully functional website that I can upload into web hosting service I use and I can easily add content and maintain myself in the future.

```html
<!DOCTYPE html>
<html lang="en">
<head>
<meta charset="utf-8">
<title>Brenholt Wealth</title>
<link href="https://fonts.googleapis.com/css2?family=Montserrat:wght@400;500;600;700&display=swap" rel="stylesheet">
<style>
:root{
  --purple:#5b2a86;
  --purple-dark:#4d2273;
  --orange:#f5a800;
  --grey:#ececec;
  --text:#222;
  --white:#fff;
  --lav:#b9a2d0;
}
*{box-sizing:border-box;margin:0;padding:0}
html,body{width:1200px;height:5141px;overflow:hidden}
body{font-family:'Montserrat',sans-serif;color:var(--text);background:var(--white);position:relative}
section,header,footer{position:absolute;left:0;width:1200px}
.abs{position:absolute}
h2.section-title{position:absolute;left:0;width:1200px;text-align:center;color:var(--purple);font-size:29px;font-weight:600;letter-spacing:.5px}
.btn{position:absolute;display:flex;align-items:center;justify-content:center;font-weight:500;color:var(--white)}
.btn-orange{background:var(--orange)}
.btn-purple{background:var(--purple)}
.photo{position:absolute}

/* header */
.site-header{top:0;height:144px;background:var(--white)}
.brand{position:absolute;left:70px;top:60px;display:flex;align-items:center;gap:10px}
.brand-dot{width:22px;height:22px;border-radius:50%;background:var(--purple)}
.brand-name{font-size:20px;font-weight:700;color:var(--purple);letter-spacing:1px}
.nav{position:absolute;top:68px;left:410px;display:flex;gap:24px;font-size:14px;font-weight:500;color:var(--purple)}
.call-btn{left:1006px;top:62px;width:110px;height:30px;font-size:13px}

/* hero */
.hero{top:144px;height:688px}
.hero .photo{inset:0;background:linear-gradient(120deg,#2a2a2e,#4a4540 45%,#6b5a44 70%,#2b2a2c)}
.hero-card{position:absolute;left:84px;top:276px;width:634px;height:336px;background:var(--white)}
.hero-card h1{position:absolute;left:44px;top:56px;font-size:40px;font-weight:700;color:var(--purple);letter-spacing:.5px}
.hero-card p{position:absolute;left:44px;top:130px;width:520px;font-size:17px;line-height:24px}
.hero-card .btn{left:28px;top:230px;width:228px;height:48px;font-size:17px}

/* intro */
.intro{top:832px;height:456px;background:var(--grey)}
.intro h2{top:108px}
.intro p{position:absolute;left:170px;width:860px;top:180px;text-align:center;font-size:20px;line-height:28px}
.intro .btn{left:496px;top:296px;width:208px;height:48px;font-size:17px}

/* about */
.about{top:1288px;height:470px;background:var(--white)}
.about .photo{left:0;top:0;width:552px;height:470px;background:linear-gradient(160deg,#3b3f3c,#1d1e1d 60%,#121212)}
.about h2{position:absolute;left:602px;top:60px;font-size:30px;font-weight:600;color:var(--purple)}
.about p{position:absolute;left:602px;top:132px;width:430px;font-size:17px;line-height:24px}
.about .btn{left:600px;top:362px;width:132px;height:38px;font-size:16px}

/* services */
.services{top:1758px;height:492px;background:var(--grey)}
.services h2{top:86px}
.service-card{position:absolute;top:208px;width:332px;height:238px;background:var(--purple);color:var(--white);text-align:center}
.service-icon{position:absolute;left:120px;top:-48px;width:92px;height:92px;border-radius:50%;background:var(--orange);border:4px solid var(--white);display:flex;align-items:center;justify-content:center}
.service-card h3{position:absolute;top:72px;width:100%;font-size:18px;font-weight:500;color:var(--orange)}
.service-card p{position:absolute;top:112px;left:24px;width:284px;font-size:17px;line-height:24px}

/* why choose */
.why{top:2250px;height:642px;background:var(--grey)}
.why h2{top:48px}
.why .photo{left:86px;top:180px;width:470px;height:344px;background:linear-gradient(160deg,#3d413d,#1e1f1e 60%,#111)}
.why-item{position:absolute;left:582px;width:520px}
.why-icon{position:absolute;left:0;top:0;width:96px;height:96px;border-radius:50%;background:var(--orange);display:flex;align-items:center;justify-content:center}
.why-item h3{position:absolute;left:108px;top:0;font-size:20px;font-weight:500;color:var(--purple)}
.why-item p{position:absolute;left:108px;top:36px;width:410px;font-size:17px;line-height:24px;color:#333}

/* schedule */
.schedule{top:2892px;height:468px}
.schedule .photo{inset:0;background:radial-gradient(ellipse at 60% 30%,#1e1e1e,#050505 70%)}
.schedule h2{position:absolute;top:106px;width:100%;text-align:center;font-size:29px;font-weight:700;color:var(--orange)}
.schedule p{position:absolute;left:160px;width:880px;top:182px;text-align:center;font-size:20px;line-height:28px;color:var(--white)}
.schedule .btn{left:514px;top:320px;width:152px;height:46px;font-size:19px}

/* different */
.different{top:3360px;height:380px;background:var(--white)}
.different h2{top:92px}
.diff-col{position:absolute;top:192px;width:320px}
.diff-col .head{display:flex;align-items:center;gap:8px;font-size:20px;font-weight:600;color:var(--orange)}
.diff-col p{margin-top:18px;font-size:15px;line-height:24px;width:290px}

/* blogs */
.blogs{top:3740px;height:480px;background:var(--white)}
.blogs h2{top:32px}
.blog-card{position:absolute;top:126px;width:210px}
.blog-card .photo{position:relative;width:208px;height:130px}
.blog-card .date{margin-top:24px;font-size:14px;color:var(--orange)}
.blog-card h3{margin-top:10px;font-size:20px;font-weight:500;color:var(--purple)}
.blog-card p{margin-top:6px;font-size:15px;line-height:24px;width:214px}

/* testimonials */
.testimonials{top:4220px;height:460px;background:var(--white)}
.testimonials h2{top:24px}
.testi{position:absolute;top:114px;width:308px;text-align:center}
.testi .box{height:188px;border:2px solid var(--lav);padding:62px 14px 0;font-size:17px;line-height:24px}
.testi .avatar{width:86px;height:86px;border-radius:50%;margin:-44px auto 0;border:2px solid var(--white)}
.testi h3{margin-top:6px;font-size:20px;font-weight:500;color:var(--purple)}
.testi .role{font-size:16px;color:var(--orange)}

/* footer */
.site-footer{top:4680px;height:461px;background:var(--purple);color:var(--white)}
.footer-logo{position:absolute;left:86px;top:172px;width:188px;height:98px;background:var(--white);display:flex;align-items:center;justify-content:center;gap:8px}
.footer-logo .brand-dot{width:14px;height:14px}
.footer-logo .brand-name{font-size:14px}
.socials{position:absolute;left:106px;top:282px;display:flex;gap:20px}
.socials span{width:34px;height:34px;border-radius:50%;border:2px solid var(--white)}
.footer-col{position:absolute;top:64px}
.footer-col h4{font-size:18px;font-weight:600;letter-spacing:.5px;padding-bottom:8px;margin-bottom:20px;display:inline-block}
.footer-col ul{list-style:none;font-size:16px;line-height:30px}
.contact h4{border-bottom:2px solid var(--white)}
.contact li{display:flex;align-items:flex-start;gap:10px;line-height:28px;width:330px;margin-bottom:10px}
.contact .ic{flex:none;width:30px;height:30px;border-radius:50%;border:2px solid var(--white);display:flex;align-items:center;justify-content:center;margin-top:-1px}
.copyright{position:absolute;left:0;top:352px;width:1200px;border-top:1px solid rgba(255,255,255,.35);padding-top:44px;text-align:center;font-size:17px}
</style>
</head>
<body>

<header class="site-header">
  <div class="brand"><span class="brand-dot"></span><span class="brand-name">BRENHOLT WEALTH</span></div>
  <nav class="nav"><span>HOME</span><span>ABOUT US</span><span>SERVICES</span><span>BLOG</span><span>TESTIMONIALS</span><span>CONTACT US</span></nav>
  <div class="btn btn-purple call-btn">CALL NOW</div>
</header>

<section class="hero">
  <div class="photo" role="img" aria-label="Photo of a smiling team of advisors gathered in a modern office"></div>
  <div class="hero-card">
    <h1>BRENHOLT WEALTH</h1>
    <p>Lorem ipsum dolor sit amet, consectetur adipiscing elit, sed do eiusmod tempor incididunt ut labore et dolore magna&nbsp; accumsan lacus vel facilisis.</p>
    <div class="btn btn-purple">Find Your Advisor</div>
  </div>
</section>

<section class="intro">
  <h2 class="section-title">HERE FOR YOU, AT EVERY STAGE OF YOUR CAREER</h2>
  <p>Lorem ipsum dolor sit amet, consectetur adipiscing elit, sed do eiusmod tempor incididunt ut labore et dolore magna aliqua. Quis ipsum suspendisse ultrices gravida.&nbsp; maecenas accumsan lacus vel facilisis.</p>
  <div class="btn btn-orange">Find Your Advisor</div>
</section>

<section class="about">
  <div class="photo" role="img" aria-label="Photo of an advisor working on a laptop in front of market data screens"></div>
  <h2>ABOUT US</h2>
  <p>Lorem ipsum dolor sit amet, consectetur adipiscing elit, sed do eiusmod tempor incididunt ut labore et dolore magna aliqua. Quis ipsum suspendisse ultrices gravida. Risus commodo viverra maecenas accumsan lacus vel facilisis. Quis ipsum suspendisse ultrices gravida. Risus commodo viverra maecenas accumsan lacus vel facilisis.</p>
  <div class="btn btn-orange">Read More</div>
</section>

<section class="services">
  <h2 class="section-title">OUR SERVICES</h2>
  <div class="service-card" style="left:82px">
    <div class="service-icon"><svg width="40" height="40" viewBox="0 0 40 40" fill="none" stroke="#fff" stroke-width="3"><path d="M8 34V22M16 34V16M24 34V20M32 34V12"/></svg></div>
    <h3>YOUNG INVESTORS</h3>
    <p>Ultrices gravida. Risus commo viverra maecenas accumsan lacus vel facilisis.</p>
  </div>
  <div class="service-card" style="left:434px">
    <div class="service-icon"><svg width="40" height="40" viewBox="0 0 40 40" fill="none" stroke="#fff" stroke-width="2.5"><path d="M6 4v30h30"/><path d="M10 28l8-10 6 6 10-14"/></svg></div>
    <h3>YOUNG INVESTORS</h3>
    <p>Ultrices gravida. Risus commo viverra maecenas accumsan lacus vel facilisis.</p>
  </div>
  <div class="service-card" style="left:786px">
    <div class="service-icon"><svg width="40" height="40" viewBox="0 0 40 40" fill="none" stroke="#fff" stroke-width="2.5"><rect x="11" y="4" width="18" height="32" rx="3"/><path d="M16 28v-4M20 28v-8M24 28v-6"/></svg></div>
    <h3>YOUNG INVESTORS</h3>
    <p>Ultrices gravida. Risus commo viverra maecenas accumsan lacus vel facilisis.</p>
  </div>
</section>

<section class="why">
  <h2 class="section-title">WHY CHOOSE US</h2>
  <div class="photo" role="img" aria-label="Video still of an advisor at a desk with market data screens">
    <svg class="abs" style="left:176px;top:132px" width="88" height="88" viewBox="0 0 88 88"><circle cx="44" cy="44" r="40" fill="none" stroke="#fff" stroke-width="5"/><path d="M35 28v32l26-16z" fill="#fff"/></svg>
  </div>
  <div class="why-item" style="top:154px">
    <div class="why-icon"><svg width="44" height="44" viewBox="0 0 44 44" fill="none" stroke="#fff" stroke-width="3"><path d="M24 4L12 24h10l-4 16 14-22H22z"/></svg></div>
    <h3>You-Focused Financial Plan</h3>
    <p>Captivating video content that shares your brand's story and resonates with your</p>
  </div>
  <div class="why-item" style="top:300px">
    <div class="why-icon"><svg width="44" height="44" viewBox="0 0 44 44" fill="none" stroke="#fff" stroke-width="3"><path d="M12 4h14l8 8v28H12z"/><circle cx="28" cy="30" r="6"/></svg></div>
    <h3>Private Clients</h3>
    <p>Optimized strategies to enhance online visibility and drive organic traffic.</p>
  </div>
  <div class="why-item" style="top:446px">
    <div class="why-icon"><svg width="48" height="48" viewBox="0 0 48 48" fill="none" stroke="#fff" stroke-width="2.5"><circle cx="24" cy="24" r="18"/><path d="M6 24h36M24 6c-8 10-8 26 0 36M24 6c8 10 8 26 0 36"/></svg></div>
    <h3>Business owners</h3>
    <p>Engaging websites expertly crafted to convert your target audience</p>
  </div>
</section>

<section class="schedule">
  <div class="photo" role="img" aria-label="Dark background photo of scattered badges and buttons"></div>
  <h2>SCHEDULE A 15 MINUTES CALL</h2>
  <p>Brenholt specializes in crafting marketing strategies that resonate with Saudi Arabian and Middle Eastern audiences. Our deep cultural insights and regional experience brand's presence in the market.</p>
  <div class="btn btn-orange">CALL NOW</div>
</section>

<section class="different">
  <h2 class="section-title">HOW WE ARE DIFFERENT</h2>
  <div class="diff-col" style="left:96px">
    <div class="head"><svg width="48" height="48" viewBox="0 0 48 48" fill="none" stroke="#f5a800" stroke-width="2"><path d="M6 30l10-10 8 6 8-8M4 38h40"/><circle cx="24" cy="12" r="6"/></svg>Dedicated Support</div>
    <p>Ensuring seamless communication and collaboration throughout your marketing journey.</p>
  </div>
  <div class="diff-col" style="left:448px">
    <div class="head"><svg width="48" height="48" viewBox="0 0 48 48" fill="none" stroke="#f5a800" stroke-width="2"><path d="M24 6a12 12 0 0 0-7 22v6h14v-6a12 12 0 0 0-7-22zM18 40h12"/></svg>Innovative Solutions</div>
    <p>Staying ahead with cutting-edge tools and technologies for brand growth.</p>
  </div>
  <div class="diff-col" style="left:810px">
    <div class="head"><svg width="48" height="48" viewBox="0 0 48 48" fill="none" stroke="#f5a800" stroke-width="2"><circle cx="30" cy="16" r="8"/><circle cx="16" cy="32" r="8"/><circle cx="30" cy="16" r="3"/><circle cx="16" cy="32" r="3"/></svg>Tailored Strategies</div>
    <p>Bespoke marketing approaches aligned with your business gotals and target audience.</p>
  </div>
</section>

<section class="blogs">
  <h2 class="section-title">OUR BLOGS</h2>
  <article class="blog-card" style="left:102px">
    <div class="photo" role="img" aria-label="Photo of glowing audio mixing screens" style="background:linear-gradient(135deg,#1c2a22,#4a3a6a 50%,#2e6a3a)"></div>
    <div class="date">Mon 13 Aug 2021</div><h3>Security Awareness</h3>
    <p>Lorem ipsum dolor sit amet, consectetur adipiscing elit, sed do eiusmod tempor</p>
  </article>
  <article class="blog-card" style="left:364px">
    <div class="photo" role="img" aria-label="Photo of hands typing on a laptop beside a coffee cup" style="background:linear-gradient(135deg,#d8d4ce,#8a8682 55%,#3a3836)"></div>
    <div class="date">Mon 13 Aug 2021</div><h3>Testing</h3>
    <p>Lorem ipsum dolor sit amet, consectetur adipiscing elit, sed do eiusmod tempor</p>
  </article>
  <article class="blog-card" style="left:632px">
    <div class="photo" role="img" aria-label="Photo of a dim teal-lit room with a person at a computer" style="background:linear-gradient(135deg,#0f3a44,#1a5a66 50%,#0a2028)"></div>
    <div class="date">Mon 13 Aug 2021</div><h3>Simulization</h3>
    <p>Lorem ipsum dolor sit amet, consectetur adipiscing elit, sed do eiusmod tempor</p>
  </article>
  <article class="blog-card" style="left:896px">
    <div class="photo" role="img" aria-label="Photo of a dark workspace with green monitor glow" style="background:linear-gradient(135deg,#1a2a1e,#3a4a3a 50%,#5a3a2a)"></div>
    <div class="date">Mon 13 Aug 2021</div><h3>Valueability</h3>
    <p>Lorem ipsum dolor sit amet, consectetur adipiscing elit, sed do eiusmod tempor</p>
  </article>
</section>

<section class="testimonials">
  <h2 class="section-title">CLIENT TESTIMONIALS</h2>
  <div class="testi" style="left:92px">
    <div class="box">“Lorem ipsum dolor sit amet consectetur adipiscing elitsed do eiusmod tempor”</div>
    <div class="avatar" role="img" aria-label="Client portrait" style="background:linear-gradient(135deg,#c0202a,#2a1a3a)"></div>
    <h3>Marlon Tessit</h3><div class="role">Director</div>
  </div>
  <div class="testi" style="left:446px">
    <div class="box">“Lorem ipsum dolor sit amet consectetur adipiscing elitsed do eiusmod tempor”</div>
    <div class="avatar" role="img" aria-label="Client portrait" style="background:linear-gradient(135deg,#e8e2da,#6a4a36)"></div>
    <h3>Ilsa Varrow</h3><div class="role">Director</div>
  </div>
  <div class="testi" style="left:798px">
    <div class="box">“Lorem ipsum dolor sit amet consectetur adipiscing elitsed do eiusmod tempor”</div>
    <div class="avatar" role="img" aria-label="Client portrait" style="background:linear-gradient(135deg,#dcdcdc,#4a4a4a)"></div>
    <h3>Otto Brevane</h3><div class="role">Director</div>
  </div>
</section>

<footer class="site-footer">
  <div class="footer-logo"><span class="brand-dot"></span><span class="brand-name">BRENHOLT WEALTH</span></div>
  <div class="socials"><span></span><span></span><span></span></div>
  <div class="footer-col" style="left:312px">
    <h4>QUICK LINKS</h4>
    <ul><li>Home</li><li>About Us</li><li>Services</li><li>Our Blogs</li><li>Testimonials</li><li>Contct Us</li></ul>
  </div>
  <div class="footer-col" style="left:568px">
    <h4>FEATURES</h4>
    <ul><li>Alerts</li><li>Areas</li><li>Maps</li><li>Notes</li><li>Photos</li><li>Permissions</li></ul>
  </div>
  <div class="footer-col contact" style="left:800px">
    <h4>CONTACT US</h4>
    <ul>
      <li><span class="ic"><svg width="14" height="14" viewBox="0 0 14 14" fill="none" stroke="#fff" stroke-width="1.5"><rect x="1" y="3" width="12" height="8"/><path d="M1 3l6 5 6-5"/></svg></span>info@brenholtwealth.com</li>
      <li><span class="ic"><svg width="14" height="14" viewBox="0 0 14 14" fill="none" stroke="#fff" stroke-width="1.5"><path d="M3 1l3 3-2 2a8 8 0 0 0 4 4l2-2 3 3-2 2C6 13 1 8 1 3z"/></svg></span>0207 555 0148, 0207 555 0193</li>
      <li><span class="ic"><svg width="14" height="14" viewBox="0 0 14 14" fill="none" stroke="#fff" stroke-width="1.5"><path d="M7 13s-4-4-4-7a4 4 0 0 1 8 0c0 3-4 7-4 7z"/><circle cx="7" cy="6" r="1.5"/></svg></span>Address Section the dummy address here</li>
    </ul>
  </div>
  <div class="copyright">All rights reserved.@ Copyrights 2023</div>
</footer>

</body>
</html>
```